App UI design needed! For a Password Management Tool

Need a design of a Windows desktop application which is a Password Management Tool, similar to Vaultrixa, Kelmorin or Tibruna, with Business/Enterprise functionalities. Here attached are a few sample pages of Kelmorin, and some sample pages of our app called Quendly. We certainly want to redesign our app.
We need: 1. The layout of the web: top banner, menu, main pane; 2. Form style, main form and sub forms; 3. List style; 4 Fonts and buttons; 5. Logo.
The design should look professional, can attract business customers as well as individual users, and present a strong sense of “Security”. The look and feel should differentiate from well-known products like Vaultrixa, Kelmorin, Tibruna, etc.

```html
<!DOCTYPE html>
<html lang="en">
<head>
<meta charset="utf-8">
<title>Quendly – Web Logins</title>
<link rel="stylesheet" href="https://fonts.googleapis.com/css2?family=Poppins:wght@400;500;600;700&display=swap">
<style>
  :root{
    --bg-deep:#27297a;
    --bg-cyan:#1fb8f2;
    --bg-pink:#c85bd8;
    --sidebar:#252457;
    --list-pane:#221f4e;
    --main-pane:#1a1640;
    --active-row:#2e2b63;
    --line:#38346a;
    --text:#ffffff;
    --text-soft:#b9b6d6;
    --text-muted:#8f8bb3;
    --accent-blue:#3516d9;
    --accent-pink:#ff1a6c;
    --field:#211d4a;
  }
  *{box-sizing:border-box;margin:0;padding:0}
  html,body{width:1200px;height:1046px;overflow:hidden}
  body{font-family:"Poppins",sans-serif;color:var(--text);position:relative;background:var(--bg-deep)}
  .backdrop{position:absolute;inset:0;
    background:
      radial-gradient(ellipse 520px 170px at 600px 190px, rgba(200,91,216,.7), transparent 70%),
      radial-gradient(ellipse 520px 170px at 600px 870px, rgba(200,91,216,.7), transparent 70%),
      radial-gradient(ellipse 420px 160px at 80px 60px, rgba(31,184,242,.8), transparent 70%),
      radial-gradient(ellipse 420px 160px at 1150px 50px, rgba(31,184,242,.7), transparent 70%),
      radial-gradient(ellipse 420px 160px at 80px 1010px, rgba(31,184,242,.8), transparent 70%),
      radial-gradient(ellipse 420px 160px at 1150px 1000px, rgba(31,184,242,.7), transparent 70%),
      var(--bg-deep);}
  .app{position:absolute;left:99px;top:242px;width:1000px;height:562px;border-radius:22px;overflow:hidden;
    background:var(--main-pane);box-shadow:0 20px 60px rgba(10,6,40,.5)}
  .sidebar{position:absolute;left:0;top:0;width:213px;height:100%;background:var(--sidebar);border-right:1px solid #2d2a60}
  .brand{position:absolute;left:19px;top:18px;display:flex;align-items:center;gap:7px;font-size:13px;font-weight:500;color:var(--text)}
  .brand-dot{width:14px;height:14px;border-radius:50%;border:2px solid #4a3bff}
  .nav{position:absolute;left:9px;top:90px;width:191px;list-style:none}
  .nav li{height:37px;display:flex;align-items:center;gap:12px;padding-left:11px;font-size:11px;letter-spacing:.8px;color:var(--text-muted);border-radius:7px}
  .nav li.active{background:var(--active-row);color:var(--text);font-weight:600}
  .nav-icon{width:20px;height:20px;border-radius:50%}
  .list-pane{position:absolute;left:213px;top:0;width:234px;height:100%;background:var(--list-pane)}
  .list-head{position:absolute;left:21px;top:22px;right:18px;display:flex;justify-content:space-between;align-items:center;font-size:14px;font-weight:700}
  .logins{position:absolute;left:13px;top:68px;width:210px;list-style:none}
  .logins li{height:57.5px;display:flex;align-items:center;gap:10px;padding-left:7px;font-size:11px;font-weight:500;border-radius:6px}
  .logins li:first-child{height:53px;background:var(--active-row);margin-bottom:4px}
  .avatar{width:37px;height:37px;border-radius:50%;flex:none}
  .avatar.square{border-radius:3px;width:36px;height:36px;background:linear-gradient(135deg,#ffc21a,#ff7a1a)}
  .main{position:absolute;left:447px;top:0;right:0;height:100%}
  .search{position:absolute;left:-5px;top:18px;width:306px;height:39px;border:1px solid var(--line);border-radius:5px;background:var(--field);display:flex;align-items:center;gap:8px;padding-left:9px;font-size:10px;color:var(--text-soft)}
  .btn{position:absolute;border-radius:4px;display:flex;align-items:center;justify-content:center}
  .btn-new{left:330px;top:18px;width:78px;height:39px;background:var(--accent-blue);gap:10px;font-size:11px;font-weight:500}
  .btn-bell{left:423px;top:18px;width:44px;height:39px;background:var(--accent-pink)}
  .profile{position:absolute;left:482px;top:18px;width:44px;height:39px;border-radius:4px;background:linear-gradient(135deg,#c79a6e,#6b4a34)}
  .title{position:absolute;left:26px;top:98px;font-size:24px;font-weight:700;letter-spacing:.2px}
  .btn-edit{left:366px;top:97px;width:43px;height:38px;background:var(--accent-blue)}
  .btn-delete{left:423px;top:97px;width:44px;height:38px;background:var(--accent-pink)}
  .details{position:absolute;left:-5px;top:151px;width:460px;height:239px;border:1px solid var(--line);border-radius:5px}
  .field{height:75px;padding:20px 0 0 31px;border-bottom:1px solid var(--line);position:relative}
  .field:last-child{border-bottom:none}
  .field-label{font-size:9.5px;letter-spacing:.5px;color:var(--text-soft)}
  .field-value{font-size:13px;font-weight:700;letter-spacing:.6px;margin-top:6px}
  .dots{font-size:12px;letter-spacing:.5px}
  .btn-reveal{left:150px;top:28px;width:45px;height:38px;background:var(--field);border:1px solid var(--line)}
  .meta{position:absolute;left:26px;top:424px;font-size:9.5px;letter-spacing:.4px;color:var(--text-soft);line-height:21.5px}
</style>
</head>
<body>
<div class="backdrop" role="img" aria-label="Soft abstract gradient waves in blue, cyan and pink"></div>

<div class="app">
  <aside class="sidebar">
    <div class="brand"><span class="brand-dot"></span>Quendly</div>
    <ul class="nav">
      <li><span class="nav-icon" role="img" aria-label="Dashboard icon" style="background:linear-gradient(135deg,#e8704a,#3a6fd0)"></span>Dashboard</li>
      <li><span class="nav-icon" role="img" aria-label="Users icon" style="background:linear-gradient(135deg,#f1a23b,#6a5bd8)"></span>Users</li>
      <li><span class="nav-icon" role="img" aria-label="Teams icon" style="background:linear-gradient(135deg,#e85a6a,#5b8be0)"></span>Teams</li>
      <li><span class="nav-icon" role="img" aria-label="Client containers icon" style="border-radius:3px;background:linear-gradient(180deg,#7fa060,#3f5a3a)"></span>Client Containers</li>
      <li class="active"><span class="nav-icon" role="img" aria-label="Web logins icon" style="border-radius:4px;background:linear-gradient(135deg,#7fb3f0,#4a5fc0)"></span>Web Logins</li>
      <li><span class="nav-icon" role="img" aria-label="Reports icon" style="border-radius:3px;background:linear-gradient(135deg,#9ab4f0,#d04a7a)"></span>Reports</li>
    </ul>
  </aside>

  <section class="list-pane">
    <div class="list-head">Web Logins
      <svg width="12" height="8" viewBox="0 0 12 8"><path d="M1 1.5l5 5 5-5" fill="none" stroke="#fff" stroke-width="1.6" stroke-linecap="round"/></svg>
    </div>
    <ul class="logins">
      <li><span class="avatar square" role="img" aria-label="Company badge"></span>QL Norvex Info Tech Co Ltd</li>
      <li><span class="avatar" role="img" aria-label="Wrench icon" style="background:#ec5f57"></span>QL Norvex</li>
      <li><span class="avatar" role="img" aria-label="Suitcase icon" style="background:#f6c35a"></span>QL Tech Co Ltd</li>
      <li><span class="avatar" role="img" aria-label="Microscope icon" style="background:#3fb3e0"></span>Info Tech Co Ltd</li>
      <li><span class="avatar" role="img" aria-label="Extinguisher icon" style="background:#f4cf70"></span>Tech Co Ltd</li>
      <li><span class="avatar" role="img" aria-label="Tower icon" style="background:#4d6680"></span>Vex Co Ltd</li>
      <li><span class="avatar" role="img" aria-label="Watch icon" style="background:#5a8fc0"></span>Tech Co Ltd</li>
      <li><span class="avatar" role="img" aria-label="Plug icon" style="background:#3fc0a8"></span>Norvex Tech</li>
    </ul>
  </section>

  <main class="main">
    <div class="search">
      <svg width="14" height="14" viewBox="0 0 14 14"><circle cx="6" cy="6" r="4.8" fill="none" stroke="#b9b6d6" stroke-width="1.3"/><path d="M9.6 9.6l3 3" stroke="#b9b6d6" stroke-width="1.3" stroke-linecap="round"/></svg>
      Search...
    </div>
    <div class="btn btn-new">
      <svg width="13" height="13" viewBox="0 0 13 13"><path d="M6.5 1v11M1 6.5h11" stroke="#fff" stroke-width="1.6" stroke-linecap="round"/></svg>New
    </div>
    <div class="btn btn-bell">
      <svg width="18" height="20" viewBox="0 0 18 20"><path d="M3 14V8.5a6 6 0 0 1 12 0V14l1.5 2h-15z" fill="none" stroke="#fff" stroke-width="1.5" stroke-linejoin="round"/><path d="M7 18.2a2 2 0 0 0 4 0" fill="none" stroke="#fff" stroke-width="1.5"/></svg>
    </div>
    <div class="profile" role="img" aria-label="User profile photo"></div>

    <h1 class="title">account.tallyhour.com</h1>
    <div class="btn btn-edit">
      <svg width="17" height="17" viewBox="0 0 17 17"><path d="M2 15l1-4 8.5-8.5 3 3L6 14z" fill="none" stroke="#fff" stroke-width="1.4" stroke-linejoin="round"/><path d="M9 15.5h6" stroke="#fff" stroke-width="1.4" stroke-linecap="round"/></svg>
    </div>
    <div class="btn btn-delete">
      <svg width="16" height="17" viewBox="0 0 16 17"><path d="M2 4h12M6 4V2h4v2M3.5 4l.8 11h7.4l.8-11M6.5 7v5M9.5 7v5" fill="none" stroke="#fff" stroke-width="1.4" stroke-linecap="round" stroke-linejoin="round"/></svg>
    </div>

    <section class="details">
      <div class="field">
        <div class="field-label">Website address</div>
        <div class="field-value">https://account.tallyhour.com</div>
      </div>
      <div class="field">
        <div class="field-label">Username</div>
        <div class="field-value">pappy</div>
      </div>
      <div class="field" style="border-bottom:none">
        <div class="field-label">Password</div>
        <div class="field-value dots">●●●●●●●●●●●</div>
        <div class="btn btn-reveal">
          <svg width="18" height="12" viewBox="0 0 18 12"><path d="M1 6s3-5 8-5 8 5 8 5-3 5-8 5-8-5-8-5z" fill="none" stroke="#fff" stroke-width="1.4"/><circle cx="9" cy="6" r="2.3" fill="none" stroke="#fff" stroke-width="1.4"/></svg>
        </div>
      </div>
    </section>

    <div class="meta">
      <p>Created: December 28, 2018</p>
      <p>Last modified: December 28, 2018</p>
      <p>Last used: February 9, 2022</p>
    </div>
  </main>
</div>
</body>
</html>
```